ZRD Roofing Billboard Design

Looking for a fresh new billboard design with my new headshot photo and using some info from my previous billboard and maybe website for design/content inspiration. My website is https://zrdroofing.com/

Also attached are my logo and current lawn sign design. I am looking for something simple, clean and modern. The landing page website should be 3816tops.com like my previous billboard has.

```html
<!DOCTYPE html>
<html lang="en">
<head>
<meta charset="utf-8">
<title>ZRD Roofing Billboard</title>
<link href="https://fonts.googleapis.com/css2?family=Oswald:wght@500;600;700&family=Roboto+Condensed:wght@700&display=swap" rel="stylesheet">
<style>
  :root {
    --page-bg: #e6e6e6;
    --navy: #1f3560;
    --navy-dark: #192b50;
    --green: #45b653;
    --white: #ffffff;
    --photo-light: #eef0f1;
    --photo-mid: #a9afb3;
    --photo-dark: #6e7479;
    --shirt: #c9d6ea;
  }
  * { margin: 0; padding: 0; box-sizing: border-box; }
  html, body { width: 1200px; height: 1200px; overflow: hidden; background: var(--page-bg); }
  .billboard {
    position: absolute; left: 40px; top: 437px; width: 1120px; height: 326px;
    background: var(--white); overflow: hidden;
    box-shadow: 0 14px 22px rgba(0,0,0,0.22);
  }
  .photo {
    position: absolute; left: 470px; top: 0; width: 650px; height: 262px;
    background:
      linear-gradient(90deg, var(--white) 0%, rgba(255,255,255,0) 14%),
      radial-gradient(ellipse 120px 150px at 420px 200px, var(--shirt) 0%, rgba(201,214,234,0) 100%),
      linear-gradient(180deg, var(--photo-mid) 0%, var(--photo-dark) 55%, var(--photo-mid) 100%);
  }
  .photo::after {
    content: ""; position: absolute; right: 0; top: 0; width: 240px; height: 100%;
    background: linear-gradient(90deg, rgba(238,240,241,0) 0%, var(--photo-light) 45%);
  }
  .bands { position: absolute; left: 0; top: 0; }
  .headline { position: absolute; left: 16px; font-family: 'Oswald', sans-serif; line-height: 1; text-transform: uppercase; }
  .headline-main { top: 4px; font-size: 108px; font-weight: 600; color: var(--navy); }
  .headline-sub { top: 118px; font-size: 64px; font-weight: 600; color: var(--green); letter-spacing: 6.5px; }
  .offer-label { position: absolute; left: 18px; font-family: 'Oswald', sans-serif; font-weight: 500; color: var(--white); line-height: 1; }
  .offer-starting { top: 205px; font-size: 47px; }
  .offer-at { top: 262px; left: 158px; font-size: 47px; }
  .offer-rule { position: absolute; left: 38px; width: 108px; height: 4px; background: var(--white); }
  .offer-rule.first { top: 287px; }
  .offer-rule.second { top: 302px; }
  .offer-price { position: absolute; left: 232px; top: 205px; font-family: 'Oswald', sans-serif; font-weight: 600; font-size: 96px; line-height: 1; color: var(--green); }
  .contact { position: absolute; top: 276px; display: flex; align-items: center; gap: 10px;
    font-family: 'Roboto Condensed', sans-serif; font-weight: 700; font-size: 35px; line-height: 1; color: var(--navy); }
  .contact svg { width: 26px; height: 26px; }
  .contact-web { left: 522px; }
  .contact-phone { left: 820px; }
  .brand { position: absolute; left: 900px; top: 40px; display: flex; flex-direction: column; align-items: center; gap: 12px; }
  .brand-name { font-family: 'Oswald', sans-serif; font-weight: 500; font-size: 28px; color: var(--navy); line-height: 1; }
  .brand-dot { width: 76px; height: 76px; border-radius: 50%; background: var(--green); }
</style>
</head>
<body>
  <div class="billboard">
    <div class="photo" role="img" aria-label="Aerial photo of a house roof with a smiling roofer headshot in a light blue shirt"></div>

    <svg class="bands" width="1120" height="326" viewBox="0 0 1120 326" aria-hidden="true">
      <defs>
        <linearGradient id="navyBand" x1="0" y1="0" x2="1" y2="0">
          <stop offset="0" stop-color="#1f3560"/>
          <stop offset="1" stop-color="#223b6b"/>
        </linearGradient>
      </defs>
      <polygon points="0,197 545,197 495,326 0,326" fill="url(#navyBand)"/>
      <polygon points="300,326 420,197 460,197 340,326" fill="#26406f" opacity="0.6"/>
      <polygon points="380,326 500,197 520,197 400,326" fill="#26406f" opacity="0.5"/>
      <polygon points="505,262 1120,262 1120,326 480,326" fill="#45b653"/>
    </svg>

    <div class="headline headline-main">Full Roof</div>
    <div class="headline headline-sub">Replacements</div>

    <div class="offer-label offer-starting">STARTING</div>
    <div class="offer-rule first"></div>
    <div class="offer-rule second"></div>
    <div class="offer-label offer-at">AT</div>
    <div class="offer-price">$7,499</div>

    <div class="contact contact-web">
      <svg viewBox="0 0 24 24" fill="none" stroke="#1f3560" stroke-width="2"><circle cx="12" cy="12" r="10"/><ellipse cx="12" cy="12" rx="4.5" ry="10"/><line x1="2" y1="12" x2="22" y2="12"/></svg>
      <span>3816tops.com</span>
    </div>
    <div class="contact contact-phone">
      <svg viewBox="0 0 24 24" fill="none" stroke="#1f3560" stroke-width="2" stroke-linejoin="round"><path d="M5 3h4l2 5-2.5 1.5a11 11 0 0 0 6 6L16 13l5 2v4a2 2 0 0 1-2 2A16 16 0 0 1 3 5a2 2 0 0 1 2-2z"/></svg>
      <span>(555) 214-7730</span>
    </div>

    <div class="brand">
      <div class="brand-name">ZRD Roofing LLC</div>
      <div class="brand-dot"></div>
    </div>
  </div>
</body>
</html>
```